TK & LJ Shearing Pty Ltd

We already have an existing logo created by Lumen Guild however we have restructured to a company. We would like someone to add Pty Ltd to our business name please.

Colors

Designer to choose only greyscale colors for use in the design.

```html
<!DOCTYPE html>
<html lang="en">
<head>
<meta charset="UTF-8">
<title>TK &amp; LJ Shearing Pty Ltd – Business Card</title>
<link href="https://fonts.googleapis.com/css2?family=Poppins:wght@400;500&display=swap" rel="stylesheet">
<style>
  :root {
    --backdrop: #1c1c1c;
    --card: #141414;
    --card-edge: #262626;
    --ink-bright: #f2f2f2;
    --ink-mid: #bdbdbd;
    --ink-soft: #8a8a8a;
    --rule: #4a4a4a;
  }
  * { margin: 0; padding: 0; box-sizing: border-box; }
  html, body {
    width: 1200px; height: 800px; overflow: hidden;
    background: var(--backdrop);
    font-family: "Poppins", sans-serif;
  }
  .canvas {
    position: relative; width: 1200px; height: 800px;
  }
  .card {
    position: absolute; left: 330px; width: 540px; height: 310px;
    background: var(--card);
    border: 1px solid var(--card-edge);
    box-shadow: 0 10px 30px rgba(0,0,0,0.5);
  }
  .card--front { top: 70px; }
  .card--back { top: 420px; }

  .wordmark {
    font-weight: 500; color: var(--ink-bright);
    letter-spacing: 0.02em; white-space: nowrap;
  }
  .card--front .wordmark {
    position: absolute; left: 0; right: 0; top: 136px;
    text-align: center; font-size: 26px; color: #5a5a5a;
  }
  .card--back .wordmark {
    position: absolute; right: 34px; top: 36px; font-size: 17px;
  }

  .rule {
    position: absolute; height: 1px; background: var(--rule);
  }
  .rule--top { left: 150px; right: 34px; top: 150px; }
  .rule--bottom { left: 34px; width: 200px; top: 232px; }

  .address {
    position: absolute; right: 34px; top: 164px; text-align: right;
    font-size: 11px; line-height: 1.45; color: var(--ink-bright);
  }
  .address .company { color: var(--ink-mid); }

  .person { position: absolute; left: 34px; top: 184px; }
  .person .name { font-size: 15px; color: var(--ink-soft); }
  .person .role { font-size: 10px; color: var(--ink-bright); margin-top: 2px; }

  .contacts {
    position: absolute; left: 34px; top: 244px; list-style: none;
    font-size: 11px; line-height: 1.5; color: var(--ink-bright);
  }
  .contacts li { display: flex; align-items: center; gap: 8px; }
  .contacts svg { width: 8px; height: 8px; fill: var(--ink-soft); }
</style>
</head>
<body>
<main class="canvas">
  <section class="card card--front" aria-label="Card front">
    <div class="wordmark">TK &amp; LJ SHEARING PTY LTD</div>
  </section>

  <section class="card card--back" aria-label="Card back">
    <div class="wordmark">TK &amp; LJ SHEARING PTY LTD</div>
    <div class="rule rule--top"></div>
    <address class="address">
      <div class="company">TK &amp; LJ Shearing Pty Ltd</div>
      <div>PO Box 418</div>
      <div>Merredin WA 6415</div>
    </address>
    <div class="person">
      <div class="name">Daniel Hart</div>
      <div class="role">President</div>
    </div>
    <div class="rule rule--bottom"></div>
    <ul class="contacts">
      <li>
        <svg viewBox="0 0 10 10"><path d="M2 0.5 L3.6 0.5 L4.3 2.8 L3.2 3.6 Q4.2 5.8 6.4 6.8 L7.2 5.7 L9.5 6.4 L9.5 8 Q9.5 9.5 8 9.5 Q0.5 9 0.5 2 Q0.5 0.5 2 0.5 Z"/></svg>
        Ray 0412555018
      </li>
      <li>
        <svg viewBox="0 0 10 10"><path d="M0.5 2 H9.5 V8.5 H0.5 Z M0.5 2 L5 5.5 L9.5 2" stroke="#8a8a8a" stroke-width="0" /><path d="M0.5 2.2 L5 5.4 L9.5 2.2 V8.5 H0.5 Z M0.7 1.5 H9.3 L5 4.6 Z"/></svg>
        tkshearing@mailbox.com
      </li>
      <li>
        <svg viewBox="0 0 10 10"><circle cx="5" cy="5" r="4.5"/></svg>
        www.tkljshearing.com
      </li>
    </ul>
  </section>
</main>
</body>
</html>
```